Retirement Community Letterhead design needed to include our new logo

We recently updated our logo and need a new letterhead to go with it. Would like the letterhead to be clean, classic, and easy to read. I've attached our current logo and a copy of our old letterhead for reference.

If possible, we would like, "Where Neighbors Belong" to be included in someway.

Ashbrook Faith Meadows is a faith-based, not-for profit senior living community offering Independent Living, Assisted Living, and a Health Care Center.

Target Market(s)

45+ Women

Industry/Entity Type

Community

Colors
00a990

Requirements
Must have
• Must be clean and elegant.
• Font used must coordinate well with the Trajan Pro font in logo
Should not have
• No crazy graphics or details.

```html
<!DOCTYPE html>
<html lang="en">
<head>
<meta charset="utf-8">
<title>Ashbrook Faith Meadows Letterhead</title>
<link href="https://fonts.googleapis.com/css2?family=Cinzel:wght@400;600&family=Poppins:wght@400&family=Montserrat:wght@600&display=swap" rel="stylesheet">
<style>
  :root {
    --backdrop: #c9c9c9;
    --paper: #ffffff;
    --ink: #3b3b3b;
    --ink-dark: #1f1f1f;
    --brand-green: #3f7d3a;
    --accent-teal: #00a990;
    --rule: #8a8a8a;
  }
  * { margin: 0; padding: 0; box-sizing: border-box; }
  html, body { width: 1200px; height: 1200px; overflow: hidden; background: var(--backdrop); }
  .letterhead {
    position: absolute; left: 200px; top: 35px; width: 800px; height: 1130px;
    background: var(--paper); box-shadow: 0 6px 24px rgba(0,0,0,0.18);
    color: var(--ink);
  }
  .brand {
    position: absolute; left: 70px; top: 70px; display: flex; align-items: center; gap: 12px;
    font-family: "Cinzel", serif; font-weight: 600; color: var(--brand-green);
  }
  .brand-dot { width: 16px; height: 16px; border-radius: 50%; background: var(--brand-green); }
  .brand-name { font-size: 22px; line-height: 1.15; letter-spacing: 1px; }
  .sender { position: absolute; right: 60px; top: 150px; text-align: right; font-family: "Cinzel", serif; }
  .sender-name { font-size: 20px; color: var(--ink-dark); font-weight: 600; }
  .sender-title { font-size: 9px; color: var(--accent-teal); margin-left: 4px; }
  .sender-contact { display: flex; justify-content: flex-end; gap: 18px; margin-top: 8px; font-size: 10px; line-height: 1.4; color: var(--ink); }
  .sender-divider { width: 4px; border-left: 1px solid var(--ink); border-right: 1px solid var(--ink); margin: 2px 0; }
  .recipient { position: absolute; left: 70px; top: 265px; }
  .recipient-label { font-family: "Cinzel", serif; font-size: 17px; color: var(--ink-dark); }
  .recipient-name { font-family: "Montserrat", sans-serif; font-weight: 600; font-size: 15px; color: var(--ink-dark); margin-top: 6px; }
  .body-copy { position: absolute; left: 70px; top: 335px; width: 670px; font-family: "Poppins", sans-serif; font-size: 11.5px; line-height: 1.5; color: var(--ink); }
  .body-copy p { margin-bottom: 14px; text-align: justify; }
  .signature { position: absolute; left: 70px; top: 860px; width: 220px; }
  .signature-mark { width: 220px; height: 52px; background: #efefef; }
  .signature-rule { height: 1px; background: var(--rule); margin-top: 6px; }
  .signature-title { font-family: "Cinzel", serif; font-size: 11px; color: var(--ink-dark); margin-top: 8px; }
  .tagline { position: absolute; left: 60px; right: 60px; top: 1030px; height: 40px; }
</style>
</head>
<body>
  <main class="letterhead">
    <div class="brand">
      <span class="brand-dot"></span>
      <span class="brand-name">Ashbrook<br>Faith Meadows</span>
    </div>

    <div class="sender">
      <div class="sender-name">Daniel Whitcombe,<span class="sender-title">Executive Director</span></div>
      <div class="sender-contact">
        <div>48 Meadowlark Lane<br>Fairview, Ohio 43010-2200</div>
        <div class="sender-divider"></div>
        <div>Office: (555) 201-4410<br>Fax: (555) 201-4411</div>
      </div>
    </div>

    <div class="recipient">
      <div class="recipient-label">To</div>
      <div class="recipient-name">Laura Bennett, CEO, NORTHFIELD PARTNERS</div>
    </div>

    <section class="body-copy">
      <p>Lorem ipsum dolor sit amet, an habeo errem euismod pri. Per id tation exerci lucilius. Usu at congue interesset, est explicari moderatius et, id pro esse docendi. Mea ancillae mentitum atomorum ne, eum congue ponderum eu. Ut mei quidam detraxit similique, dissentias omittantur ut mei.</p>
      <p>Cu nec purto accusam, aliquid graecis disputando quo cu, id augue affert nam. Ex quo cibo iuvaret explicari. In postea disputationi mea, meliore recusabo hendrerit ius et, alienum molestie torquatos vel et. Nam virtute recteque inciderint ei. Sed clita similique quaerendum ut, ex dolorem constituto eos, cu elit elitr ancillae eos. Virtute mentitum invidunt mea te. Qui quis tollit disputando cu, modus melius ne mel.</p>
      <p>Duo oportere petentium in, odio putant placerat usu ad. Vis ut error electram, id placerat singulis postulant his, pri graecis accommodare at. Ut qui ignota inermis partiendo, vis maiestatis abhorreant ei, cu utinam posidonium eam. Mel odio nibh delenit ei, vel ad quodsi impetus explicari. Te mea facilis recteque, harum munere nostrud ea usu. Alii meis est ne, eos consul mucius forensibus te.</p>
      <p>Cu nec purto accusam, aliquid graecis disputando quo cu, id augue affert nam. Ex quo cibo iuvaret explicari. In postea disputationi mea, meliore recusabo hendrerit ius et, alienum molestie torquatos vel et. Nam virtute recteque inciderint ei. Sed clita similique quaerendum ut, ex dolorem constituto eos, cu elit elitr ancillae eos. Virtute mentitum invidunt mea te. Qui quis tollit disputando cu, modus melius ne mel.</p>
      <p>Lorem ipsum dolor sit amet, an habeo errem euismod pri. Per id tation exerci lucilius. Usu at congue interesset, est explicari moderatius et, id pro esse docendi. Mea ancillae mentitum atomorum ne, eum congue ponderum eu. Ut mei quidam detraxit similique, dissentias omittantur ut mei.</p>
      <p>Cu nec purto accusam, aliquid graecis disputando quo cu, id augue affert nam. Ex quo cibo iuvaret explicari. In postea disputationi mea, meliore recusabo hendrerit ius et, alienum molestie torquatos vel et. Nam virtute recteque inciderint ei. Sed clita similique quaerendum ut, ex dolorem constituto eos, cu elit elitr ancillae eos. Virtute mentitum invidunt mea te. Qui quis tollit disputando cu, modus melius ne mel.</p>
    </section>

    <div class="signature">
      <div class="signature-mark" role="img" aria-label="Handwritten signature of Daniel Whitcombe"></div>
      <div class="signature-rule"></div>
      <div class="signature-title">Executive Director</div>
    </div>

    <svg class="tagline" viewBox="0 0 680 40" aria-label="Where Neighbors Belong">
      <g stroke="var(--accent-teal)" stroke-width="2" fill="var(--accent-teal)">
        <line x1="6" y1="20" x2="100" y2="20"/>
        <circle cx="6" cy="20" r="3"/>
        <circle cx="100" cy="20" r="3"/>
        <line x1="580" y1="20" x2="674" y2="20"/>
        <circle cx="580" cy="20" r="3"/>
        <circle cx="674" cy="20" r="3"/>
      </g>
      <text x="340" y="28" text-anchor="middle" font-family="Cinzel, serif" font-size="24" letter-spacing="2" fill="var(--accent-teal)">Where Neighbors Belong</text>
    </svg>
  </main>
</body>
</html>
```